Sunny Nook Snack Balls

Hello! I need the attached pdf artwork of individual pouch designs to be fit into both attached templates in a CYMK format. Each design/ flavor needs to be fit into the individual pouch template and the sea end box template. I need to artwork files to send to printing. Thank you!

Target Market(s)

Everyone who loves yummy snacks.

Font styles to use
Script
Other font styles liked:
• See attached design.

Colors

Designer to choose colors to be used in the design.

Requirements
Must have
• Designs must fit attached templates, bleed areas, be in the correct format, etc. The tan areas on the side if the packages are a place holder for the kraft material the design will be printed on. The box template design and individual pouch template need to be cohesive.
Nice to have
• Think Vornel Bar but brighter,
Should not have
• Designs cannot be made to not fit the attached templates.

```html
<!DOCTYPE html>
<html lang="en">
<head>
<meta charset="utf-8">
<title>Sunny Nook Snack Balls – Pouch Sheet</title>
<link href="https://fonts.googleapis.com/css2?family=Lato:wght@300;400;700&family=Special+Elite&display=swap" rel="stylesheet">
<style>
  :root{
    --kraft:#fde9de;
    --trim:#5ba4d8;
    --fold:#c9b8ae;
    --paper:#ffffff;
    --ink:#231f20;
    --choco:#00bef2;
    --pbj:#8c62aa;
    --maple:#f26663;
    --nut:#a3cf62;
    --straw:#ee3124;
    --dark:#ee5397;
    --sans:'Lato', sans-serif;
    --type:'Special Elite', monospace;
  }
  *{box-sizing:border-box;margin:0;padding:0}
  html,body{width:1200px;height:1200px;overflow:hidden;background:#fff}
  .sheet{position:absolute;left:308px;top:25px;width:590px;height:1158px;border:1px solid var(--trim)}
  .pouch{position:relative;width:100%;height:193px;background:var(--kraft);border-bottom:1px solid var(--trim)}
  .pouch:last-child{border-bottom:none}
  .pouch__band{position:absolute;left:0;right:0;top:20px;height:151px;background:var(--flavor)}
  .pouch--choco{--flavor:var(--choco)}
  .pouch--pbj{--flavor:var(--pbj)}
  .pouch--maple{--flavor:var(--maple)}
  .pouch--nut{--flavor:var(--nut)}
  .pouch--straw{--flavor:var(--straw)}
  .pouch--dark{--flavor:var(--dark)}
  .fold{position:absolute;top:0;bottom:0;width:0;border-left:1px dashed var(--fold);opacity:.7}
  .fold--a{left:258px}.fold--b{left:334px}
  .vtext{position:absolute;top:0;height:151px;writing-mode:vertical-rl;text-align:center;color:#fff;font-family:var(--sans);white-space:nowrap}
  .up{transform:rotate(180deg)}
  .flavor-side{left:84px;width:16px;font-size:10.5px;font-weight:300;letter-spacing:.2px}
  .made{left:272px;width:16px;font-size:5px;line-height:6px;color:var(--ink)}
  .maker{left:302px;width:18px;font-size:5.2px;line-height:6.5px;color:var(--ink)}
  .weight{left:354px;width:8px;font-size:3.4px}
  .flavor-front{left:367px;width:12px;font-size:6px;font-weight:300}
  .slogan{left:382px;width:14px;font-family:var(--type);font-size:7px;letter-spacing:.6px}
  .promise{left:490px;width:16px;font-family:var(--type);font-size:5px;line-height:7px;letter-spacing:.4px}
  .datebox{position:absolute;left:287px;top:49px;width:12px;height:50px;border-radius:6px;background:var(--paper)}
  .brand{position:absolute;left:404px;top:38px;width:76px;height:76px;border-radius:50%;border:4px solid rgba(255,255,255,.55);display:flex;align-items:center;justify-content:center}
  .brand__name{transform:rotate(90deg);text-align:center;color:#fff;font-family:var(--sans);font-weight:700;font-size:7px;line-height:8px}
  .label{position:absolute;left:108px;top:20px;width:133px;height:110px;background:var(--paper)}
  .label__inner{position:absolute;left:11.5px;top:-11.5px;width:110px;height:133px;transform:rotate(-90deg);padding:4px 5px;color:var(--ink);font-family:var(--sans);font-size:2.6px;line-height:3.3px}
  .label__title{font-family:var(--type);font-size:5px;line-height:6px;margin-bottom:3px}
  .label__story{position:absolute;left:5px;top:12px;width:52px}
  .label__story p{margin-bottom:2px}
  .facts{position:absolute;left:58px;top:11px;width:48px;height:72px;border:.6px solid var(--ink);padding:1px}
  .facts__head{font-weight:700;font-size:3.6px;line-height:4px;border-bottom:1.4px solid var(--ink)}
  .facts__row{display:flex;justify-content:space-between;border-bottom:.4px solid var(--ink)}
  .facts__ingr{position:absolute;left:58px;top:86px;width:48px;font-size:2.2px;line-height:2.8px}
  .label__claims{position:absolute;left:5px;top:92px;list-style:none}
  .label__web{position:absolute;left:5px;top:124px;font-size:2.6px}
</style>
</head>
<body>
<main class="sheet">

  <section class="pouch pouch--choco">
    <div class="pouch__band"></div>
    <span class="fold fold--a"></span><span class="fold fold--b"></span>
    <div class="pouch__band" style="background:transparent">
      <p class="vtext flavor-side up">Choco Chip</p>
      <div class="label"><div class="label__inner">
        <h2 class="label__title">Take a Sunny Bite out of life!</h2>
        <div class="label__story"><p>Sunny Nook bites were made for me and for you. I wanted a real snack with simple ingredients that taste good.</p><p>Made with real and nutritious ingredients, they keep you going all day long. Take them on a run or to work.</p><p>So, here is a good snack that is also good for you. I hope you enjoy them as much as I do.</p><p>Mara</p></div>
        <div class="facts"><div class="facts__head">Nutrition Facts</div><div class="facts__row"><span>Serving size</span><span>1 pack</span></div><div class="facts__row"><span>Calories</span><span>210</span></div><div class="facts__row"><span>Total Fat</span><span>9g</span></div><div class="facts__row"><span>Sodium</span><span>60mg</span></div><div class="facts__row"><span>Carbohydrate</span><span>27g</span></div><div class="facts__row"><span>Protein</span><span>5g</span></div></div>
        <p class="facts__ingr">Ingredients: dates, oats, cocoa, almonds, sea salt.</p>
        <ul class="label__claims"><li>❖ No artificial flavorings</li><li>❖ No added sugar</li><li>❖ No funny stuff</li></ul>
        <p class="label__web">www.sunnynookbymara.com</p>
      </div></div>
      <p class="vtext made up">Made in the USA<br>BEST BY</p>
      <span class="datebox"></span>
      <p class="vtext maker up">Manufactured by Mara Quill LLC<br>Coral Bay, FL 33000</p>
      <p class="vtext weight">Net weight 1.8 oz. (51g) per pack</p>
      <p class="vtext flavor-front">Choco Chip</p>
      <p class="vtext slogan">Always the perfect bite.</p>
      <div class="brand"><p class="brand__name">Sunny Nook<br>Snack Balls</p></div>
      <p class="vtext promise">No artificial flavorings.<br>No added sugar. No funny stuff.</p>
    </div>
  </section>

  <section class="pouch pouch--pbj">
    <div class="pouch__band"></div>
    <span class="fold fold--a"></span><span class="fold fold--b"></span>
    <div class="pouch__band" style="background:transparent">
      <p class="vtext flavor-side up">Peanut Butter &amp; Jelly</p>
      <div class="label"><div class="label__inner">
        <h2 class="label__title">Take a Sunny Bite out of life!</h2>
        <div class="label__story"><p>Sunny Nook bites were made for me and for you. I wanted a real snack with simple ingredients that taste good.</p><p>Made with real and nutritious ingredients, they keep you going all day long. Take them on a run or to work.</p><p>So, here is a good snack that is also good for you. I hope you enjoy them as much as I do.</p><p>Mara</p></div>
        <div class="facts"><div class="facts__head">Nutrition Facts</div><div class="facts__row"><span>Serving size</span><span>1 pack</span></div><div class="facts__row"><span>Calories</span><span>210</span></div><div class="facts__row"><span>Total Fat</span><span>9g</span></div><div class="facts__row"><span>Sodium</span><span>60mg</span></div><div class="facts__row"><span>Carbohydrate</span><span>27g</span></div><div class="facts__row"><span>Protein</span><span>5g</span></div></div>
        <p class="facts__ingr">Ingredients: dates, oats, peanuts, berries, sea salt.</p>
        <ul class="label__claims"><li>❖ No artificial flavorings</li><li>❖ No added sugar</li><li>❖ No funny stuff</li></ul>
        <p class="label__web">www.sunnynookbymara.com</p>
      </div></div>
      <p class="vtext made up">Made in the USA<br>BEST BY</p>
      <span class="datebox"></span>
      <p class="vtext maker up">Manufactured by Mara Quill LLC<br>Coral Bay, FL 33000</p>
      <p class="vtext weight">Net weight 1.8 oz. (51g) per pack</p>
      <p class="vtext flavor-front">Peanut Butter &amp; Jelly</p>
      <p class="vtext slogan">Always the perfect bite.</p>
      <div class="brand"><p class="brand__name">Sunny Nook<br>Snack Balls</p></div>
      <p class="vtext promise">No artificial flavorings.<br>No added sugar. No funny stuff.</p>
    </div>
  </section>

  <section class="pouch pouch--maple">
    <div class="pouch__band"></div>
    <span class="fold fold--a"></span><span class="fold fold--b"></span>
    <div class="pouch__band" style="background:transparent">
      <p class="vtext flavor-side up">Maple Cinnamon</p>
      <div class="label"><div class="label__inner">
        <h2 class="label__title">Take a Sunny Bite out of life!</h2>
        <div class="label__story"><p>Sunny Nook bites were made for me and for you. I wanted a real snack with simple ingredients that taste good.</p><p>Made with real and nutritious ingredients, they keep you going all day long. Take them on a run or to work.</p><p>So, here is a good snack that is also good for you. I hope you enjoy them as much as I do.</p><p>Mara</p></div>
        <div class="facts"><div class="facts__head">Nutrition Facts</div><div class="facts__row"><span>Serving size</span><span>1 pack</span></div><div class="facts__row"><span>Calories</span><span>210</span></div><div class="facts__row"><span>Total Fat</span><span>9g</span></div><div class="facts__row"><span>Sodium</span><span>60mg</span></div><div class="facts__row"><span>Carbohydrate</span><span>27g</span></div><div class="facts__row"><span>Protein</span><span>5g</span></div></div>
        <p class="facts__ingr">Ingredients: dates, oats, maple, cinnamon, sea salt.</p>
        <ul class="label__claims"><li>❖ No artificial flavorings</li><li>❖ No added sugar</li><li>❖ No funny stuff</li></ul>
        <p class="label__web">www.sunnynookbymara.com</p>
      </div></div>
      <p class="vtext made up">Made in the USA<br>BEST BY</p>
      <span class="datebox"></span>
      <p class="vtext maker up">Manufactured by Mara Quill LLC<br>Coral Bay, FL 33000</p>
      <p class="vtext weight">Net weight 1.8 oz. (51g) per pack</p>
      <p class="vtext flavor-front">Maple Cinnamon</p>
      <p class="vtext slogan">Always the perfect bite.</p>
      <div class="brand"><p class="brand__name">Sunny Nook<br>Snack Balls</p></div>
      <p class="vtext promise">No artificial flavorings.<br>No added sugar. No funny stuff.</p>
    </div>
  </section>

  <section class="pouch pouch--nut">
    <div class="pouch__band"></div>
    <span class="fold fold--a"></span><span class="fold fold--b"></span>
    <div class="pouch__band" style="background:transparent">
      <p class="vtext flavor-side up">Health Nut</p>
      <div class="label"><div class="label__inner">
        <h2 class="label__title">Take a Sunny Bite out of life!</h2>
        <div class="label__story"><p>Sunny Nook bites were made for me and for you. I wanted a real snack with simple ingredients that taste good.</p><p>Made with real and nutritious ingredients, they keep you going all day long. Take them on a run or to work.</p><p>So, here is a good snack that is also good for you. I hope you enjoy them as much as I do.</p><p>Mara</p></div>
        <div class="facts"><div class="facts__head">Nutrition Facts</div><div class="facts__row"><span>Serving size</span><span>1 pack</span></div><div class="facts__row"><span>Calories</span><span>210</span></div><div class="facts__row"><span>Total Fat</span><span>9g</span></div><div class="facts__row"><span>Sodium</span><span>60mg</span></div><div class="facts__row"><span>Carbohydrate</span><span>27g</span></div><div class="facts__row"><span>Protein</span><span>5g</span></div></div>
        <p class="facts__ingr">Ingredients: dates, oats, cashews, seeds, sea salt.</p>
        <ul class="label__claims"><li>❖ No artificial flavorings</li><li>❖ No added sugar</li><li>❖ No funny stuff</li></ul>
        <p class="label__web">www.sunnynookbymara.com</p>
      </div></div>
      <p class="vtext made up">Made in the USA<br>BEST BY</p>
      <span class="datebox"></span>
      <p class="vtext maker up">Manufactured by Mara Quill LLC<br>Coral Bay, FL 33000</p>
      <p class="vtext weight">Net weight 1.8 oz. (51g) per pack</p>
      <p class="vtext flavor-front">Health Nut</p>
      <p class="vtext slogan">Always the perfect bite.</p>
      <div class="brand"><p class="brand__name">Sunny Nook<br>Snack Balls</p></div>
      <p class="vtext promise">No artificial flavorings.<br>No added sugar. No funny stuff.</p>
    </div>
  </section>

  <section class="pouch pouch--straw">
    <div class="pouch__band"></div>
    <span class="fold fold--a"></span><span class="fold fold--b"></span>
    <div class="pouch__band" style="background:transparent">
      <p class="vtext flavor-side up">Strawberry Chocolate Coconut</p>
      <div class="label"><div class="label__inner">
        <h2 class="label__title">Take a Sunny Bite out of life!</h2>
        <div class="label__story"><p>Sunny Nook bites were made for me and for you. I wanted a real snack with simple ingredients that taste good.</p><p>Made with real and nutritious ingredients, they keep you going all day long. Take them on a run or to work.</p><p>So, here is a good snack that is also good for you. I hope you enjoy them as much as I do.</p><p>Mara</p></div>
        <div class="facts"><div class="facts__head">Nutrition Facts</div><div class="facts__row"><span>Serving size</span><span>1 pack</span></div><div class="facts__row"><span>Calories</span><span>210</span></div><div class="facts__row"><span>Total Fat</span><span>9g</span></div><div class="facts__row"><span>Sodium</span><span>60mg</span></div><div class="facts__row"><span>Carbohydrate</span><span>27g</span></div><div class="facts__row"><span>Protein</span><span>5g</span></div></div>
        <p class="facts__ingr">Ingredients: dates, oats, strawberry, cocoa, coconut.</p>
        <ul class="label__claims"><li>❖ No artificial flavorings</li><li>❖ No added sugar</li><li>❖ No funny stuff</li></ul>
        <p class="label__web">www.sunnynookbymara.com</p>
      </div></div>
      <p class="vtext made up">Made in the USA<br>BEST BY</p>
      <span class="datebox"></span>
      <p class="vtext maker up">Manufactured by Mara Quill LLC<br>Coral Bay, FL 33000</p>
      <p class="vtext weight">Net weight 1.8 oz. (51g) per pack</p>
      <p class="vtext flavor-front">Strawberry Chocolate Coconut</p>
      <p class="vtext slogan">Always the perfect bite.</p>
      <div class="brand"><p class="brand__name">Sunny Nook<br>Snack Balls</p></div>
      <p class="vtext promise">No artificial flavorings.<br>No added sugar. No funny stuff.</p>
    </div>
  </section>

  <section class="pouch pouch--dark">
    <div class="pouch__band"></div>
    <span class="fold fold--a"></span><span class="fold fold--b"></span>
    <div class="pouch__band" style="background:transparent">
      <p class="vtext flavor-side up">Dark Chocolate Sea Salt</p>
      <div class="label"><div class="label__inner">
        <h2 class="label__title">Take a Sunny Bite out of life!</h2>
        <div class="label__story"><p>Sunny Nook bites were made for me and for you. I wanted a real snack with simple ingredients that taste good.</p><p>Made with real and nutritious ingredients, they keep you going all day long. Take them on a run or to work.</p><p>So, here is a good snack that is also good for you. I hope you enjoy them as much as I do.</p><p>Mara</p></div>
        <div class="facts"><div class="facts__head">Nutrition Facts</div><div class="facts__row"><span>Serving size</span><span>1 pack</span></div><div class="facts__row"><span>Calories</span><span>210</span></div><div class="facts__row"><span>Total Fat</span><span>9g</span></div><div class="facts__row"><span>Sodium</span><span>60mg</span></div><div class="facts__row"><span>Carbohydrate</span><span>27g</span></div><div class="facts__row"><span>Protein</span><span>5g</span></div></div>
        <p class="facts__ingr">Ingredients: dates, oats, dark cocoa, almonds, sea salt.</p>
        <ul class="label__claims"><li>❖ No artificial flavorings</li><li>❖ No added sugar</li><li>❖ No funny stuff</li></ul>
        <p class="label__web">www.sunnynookbymara.com</p>
      </div></div>
      <p class="vtext made up">Made in the USA<br>BEST BY</p>
      <span class="datebox"></span>
      <p class="vtext maker up">Manufactured by Mara Quill LLC<br>Coral Bay, FL 33000</p>
      <p class="vtext weight">Net weight 1.8 oz. (51g) per pack</p>
      <p class="vtext flavor-front">Dark Chocolate Sea Salt</p>
      <p class="vtext slogan">Always the perfect bite.</p>
      <div class="brand"><p class="brand__name">Sunny Nook<br>Snack Balls</p></div>
      <p class="vtext promise">No artificial flavorings.<br>No added sugar. No funny stuff.</p>
    </div>
  </section>

</main>
</body>
</html>
```